Computer business needs new look.

KELD Computers has been selling and repairing, servicing computers in northern NSW for 20 years and has now branched out into Surveillance/ CCTV systems Alarm systems and just about anything technical.
We have also changed our area of operation from just the northern rivers to include all of outback New South Wales and Queensland.
We have changed our name slightly to K.E.L.D Sundown Technical Services.I will include my old business card.The Logo can stay or go i am open to all designs.
Updates

facebook page for info https://www.examplebook.test/pages/KELD-Computers/482019375610283?fref=ts The top half of the business card i uploaded looks pink ! it should be white

I should have mentioned this before. My new look cards will become the look of the business. ie: advertising, vehicle sign-writing etc: The look that i think im after is more to large business/corporate look not "WALLY THE FIXER " Probably the main focus is the fact that we service the small towns in outback Australia. " Billabong Barney " Not just the big city's Please feel free to through any thing at me and any questions please ask.

I have uploaded a picture that i would like the back of the card to look like. Please have a look and see what you can do.

Reason: I am hoping to get some original designs that i like. So far i have just 1 that i like..there must be more ideas out there.

Target Market(s)

Small to medium business

Industry/Entity Type

Business

Contact Information for Business Card

K.E.L.D Sundown Technical Services
Owen Pelkie
1300621745 0457 318206

Requirements
Nice to have
• Back of card to have a list of services
Computer sales
Computer Repairs & Virus removal
Wireless Hotspots
CCTV Installation and repair
Network Design and setup
Troubleshooting

```html
<!DOCTYPE html>
<html lang="en">
<head>
<meta charset="utf-8">
<title>K.E.L.D Sundown Technical Services – Business Card</title>
<link rel="stylesheet" href="https://fonts.googleapis.com/css2?family=Exo+2:wght@400;500;800&family=Michroma&display=swap">
<style>
  :root {
    --backdrop: #e6e7ea;
    --card-top: #ffffff;
    --card-mid: #f1f2f4;
    --card-low: #e4e6e9;
    --ink: #3b3f4a;
    --icon: #3d4f9e;
    --brand-blue: #1f6fd6;
    --name-indigo: #3a3c9c;
    --band-light: #3a9bea;
    --band-deep: #1264cf;
    --band-grey: #6d6f73;
  }
  * { box-sizing: border-box; margin: 0; padding: 0; }
  html, body {
    width: 1200px; height: 900px; overflow: hidden;
    background: var(--backdrop);
  }
  .canvas {
    position: relative; width: 1200px; height: 900px;
    display: flex; align-items: center; justify-content: center;
  }
  .business-card {
    position: relative; width: 960px; height: 548px;
    border-radius: 46px; overflow: hidden;
    background: linear-gradient(170deg, var(--card-top) 0%, var(--card-mid) 55%, var(--card-low) 100%);
    box-shadow: 0 18px 40px rgba(0,0,0,0.18);
    font-family: "Exo 2", sans-serif;
  }
  .card-swoosh { position: absolute; inset: 0; width: 100%; height: 100%; }

  .contact-list {
    position: absolute; left: 44px; top: 138px;
    list-style: none; color: var(--ink);
    font-size: 22px; letter-spacing: 1px;
  }
  .contact-list li { display: flex; align-items: center; height: 30px; margin-bottom: 3px; }
  .contact-list .small { font-size: 19px; letter-spacing: 0.5px; }
  .contact-icon { width: 20px; height: 20px; margin-right: 16px; fill: var(--icon); flex: none; }

  .brand {
    position: absolute; left: 390px; top: 92px;
    display: flex; align-items: center; gap: 22px;
    color: var(--brand-blue);
  }
  .brand-dot { width: 88px; height: 88px; border-radius: 50%; background: var(--brand-blue); }
  .brand-name { font-weight: 800; font-size: 64px; line-height: 1; letter-spacing: 2px; }
  .brand-tagline { font-weight: 800; font-size: 19px; margin-top: 6px; letter-spacing: 0.3px; }

  .holder {
    position: absolute; right: 130px; top: 288px; text-align: right;
  }
  .holder-name {
    font-family: "Michroma", sans-serif; font-size: 23px;
    color: var(--name-indigo); letter-spacing: 1px;
  }
  .holder-role {
    font-family: "Michroma", sans-serif; font-size: 15px;
    color: var(--ink); letter-spacing: 1.5px; margin-top: 8px;
  }
</style>
</head>
<body>
<main class="canvas">
  <section class="business-card" aria-label="K.E.L.D Sundown Technical Services business card">
    <svg class="card-swoosh" viewBox="0 0 960 548" preserveAspectRatio="none" aria-hidden="true">
      <defs>
        <linearGradient id="bandFill" x1="0" y1="0" x2="1" y2="0">
          <stop offset="0" stop-color="var(--band-light)"/>
          <stop offset="1" stop-color="var(--band-deep)"/>
        </linearGradient>
      </defs>
      <path d="M0,318 Q380,470 960,318" fill="none" stroke="var(--band-grey)" stroke-width="9"/>
      <path d="M0,338 Q400,520 960,345 L960,548 L0,548 Z" fill="url(#bandFill)"/>
      <path d="M0,372 Q430,540 960,392 L960,404 Q430,556 0,392 Z" fill="#ffffff"/>
      <path d="M960,318 Q820,360 700,388 Q840,372 960,345 Z" fill="var(--band-deep)" opacity="0.9"/>
    </svg>

    <ul class="contact-list">
      <li><svg class="contact-icon" viewBox="0 0 24 24"><path d="M6.6 10.8a15.1 15.1 0 0 0 6.6 6.6l2.2-2.2a1 1 0 0 1 1-.25 11.4 11.4 0 0 0 3.6.57 1 1 0 0 1 1 1V20a1 1 0 0 1-1 1A17 17 0 0 1 3 4a1 1 0 0 1 1-1h3.5a1 1 0 0 1 1 1c0 1.25.2 2.45.57 3.57a1 1 0 0 1-.25 1z"/></svg>012 345 6789</li>
      <li><svg class="contact-icon" viewBox="0 0 24 24"><path d="M7 1h10a2 2 0 0 1 2 2v18a2 2 0 0 1-2 2H7a2 2 0 0 1-2-2V3a2 2 0 0 1 2-2zm0 3v14h10V4zm5 15.5a1.2 1.2 0 1 0 0 2.4 1.2 1.2 0 0 0 0-2.4z"/></svg>012 345 6789</li>
      <li><svg class="contact-icon" viewBox="0 0 24 24"><path d="M6 2h9l3 3v5h2a2 2 0 0 1 2 2v9H2v-9a2 2 0 0 1 2-2h2zm2 2v6h8V6h-2V4zm-2 9v2h2v-2zm4 0v2h2v-2zm4 0v2h2v-2zm-8 4v2h2v-2zm4 0v2h2v-2zm4 0v2h2v-2z"/></svg>012 345 6789</li>
      <li class="small"><svg class="contact-icon" viewBox="0 0 24 24"><path d="M2 5h20v14H2zm2 2v.4l8 5.2 8-5.2V7zm0 2.8V17h16V9.8l-8 5.2z"/></svg>urname@email.com</li>
      <li class="small"><svg class="contact-icon" viewBox="0 0 24 24"><path d="M12 2a10 10 0 1 0 0 20 10 10 0 0 0 0-20zm6.9 6h-3a15 15 0 0 0-1.3-3.9A8 8 0 0 1 18.9 8zM12 4c.8 1.1 1.5 2.5 1.9 4h-3.8c.4-1.5 1.1-2.9 1.9-4zM4.3 14a8 8 0 0 1 0-4h3.4a16 16 0 0 0 0 4zm.8 2h3a15 15 0 0 0 1.3 3.9A8 8 0 0 1 5.1 16zm3-8h-3a8 8 0 0 1 4.3-3.9A15 15 0 0 0 8.1 8zM12 20c-.8-1.1-1.5-2.5-1.9-4h3.8c-.4 1.5-1.1 2.9-1.9 4zm2.3-6H9.7a14 14 0 0 1 0-4h4.6a14 14 0 0 1 0 4zm.3 5.9a15 15 0 0 0 1.3-3.9h3a8 8 0 0 1-4.3 3.9zm1.7-5.9a16 16 0 0 0 0-4h3.4a8 8 0 0 1 0 4z"/></svg>www.urwebsitename.com</li>
    </ul>

    <div class="brand">
      <span class="brand-dot" aria-hidden="true"></span>
      <div class="brand-text">
        <div class="brand-name">K.E.L.D</div>
        <div class="brand-tagline">Sundown Technical Services</div>
      </div>
    </div>

    <div class="holder">
      <div class="holder-name">MARCUS DELANE</div>
      <div class="holder-role">FINANCIAL ADVISOR</div>
    </div>
  </section>
</main>
</body>
</html>
```